Innovative and exciting banner advert for real estate
Lots of freedom of design
#10 I like the way the 'save thousands in commission' is done with mixed size font. The 'save thousands' stands out very clearly which is important to us
Thanks.
Hi and thank you designers for your attention to our project, there are some great ideas coming in now.
A slight change to the brief:
In the blue screen, please remove 'money back guarantee' and replace with 'no hidden charges' from the green screen so each screen has only 3 bullet points.
Thanks
RPellow
Hi Designers
Please note, we do not require the logo in the adverts just the use of the logo colours as the base.
It is more important that the first line of text stands out. If you are going to insert the logo, please make it a minor element or as #4 has cleverly used it for the bullet points.
Thanks designers for your time and great ideas. #4 I like the way you have used the logo symbol in the bullet points, and that you have aligned the bullets points to the left, it looks good.
#5 the way that 'save thousands' and 'get the best price' stand out clearly is great, this is the message that we are trying to pass on to viewers, it is most important.
If there is any information you need please contact me directly, I will check messages.
Just to clarify, we do not require the logo in the adverts just the use of the logo colours as the base. These adverts are going to be used on our own site.
Regards
Thanks Hostmod for making that clear for designers.
Designers, we don't have images of the product we sell as we provide real estate services (not goods). If looking for inspiration for imagery, residential property is more appropriate than commercial property.
Thanks everyone.
Attention Designers!
PH is looking for static banner design which includes two individual advert frames.
Banner size : 450 wide x 225 high
I'm clarifying with our site technicians exactly what the frames should be.
We originally wanted two individual advert frames, 450 wide x 225 high, with no animation in the frames themselves. However, when trying to work within the Tandelvox fields, we couldn't elect the specific size we required and instead had to opt for a package deal.
I will upload a link to the real estate website template we will be using, the template has 'featured property' images in the centre of the homepage which we will be replacing with our two adverts. That is, we will not have the featured property on the home page at all.
http://skins.brovellanstudio.example/?theme=realestate2
Dear PH,
Is this animated gifs or flash?

```html
<!DOCTYPE html>
<html lang="en">
<head>
<meta charset="utf-8">
<title>Get the best price for your property</title>
<link rel="stylesheet" href="https://fonts.googleapis.com/css2?family=Anton&family=Open+Sans:wght@700;800&display=swap">
<style>
  :root {
    --frame: #ffffff;
    --field: #1f8f22;
    --field-deep: #157a18;
    --accent: #d8f03c;
    --ink: #ffffff;
    --bar: #0d3815;
    --bar-edge: #3f7a44;
    --bullet: #9fc49c;
  }
  html, body {
    margin: 0;
    padding: 0;
    width: 1200px;
    height: 614px;
    overflow: hidden;
    background: var(--frame);
  }
  .banner {
    position: absolute;
    left: 5px;
    top: 5px;
    width: 1190px;
    height: 590px;
    background: radial-gradient(ellipse at 50% 35%, var(--field) 0%, var(--field) 55%, var(--field-deep) 100%);
    overflow: hidden;
  }
  .headline {
    position: absolute;
    left: 0;
    top: 0;
    width: 1190px;
    height: 280px;
  }
  .headline .get {
    font-family: "Anton", "Impact", sans-serif;
    fill: var(--accent);
  }
  .headline .claim {
    font-family: "Open Sans", "Arial", sans-serif;
    font-weight: 800;
    fill: var(--ink);
  }
  .benefits {
    position: absolute;
    left: 19px;
    top: 288px;
    width: 1147px;
    margin: 0;
    padding: 0;
    list-style: none;
  }
  .benefit {
    position: relative;
    height: 50px;
    margin-bottom: 12px;
    background: var(--bar);
    border: 2px solid var(--bar-edge);
    box-sizing: border-box;
    display: flex;
    align-items: center;
    font-family: "Open Sans", "Arial", sans-serif;
    font-weight: 700;
    font-size: 29px;
    letter-spacing: -0.5px;
    color: var(--ink);
  }
  .benefit::before {
    content: "";
    width: 26px;
    height: 26px;
    margin: 0 26px 0 70px;
    border-radius: 50%;
    background: var(--bullet);
    flex: none;
  }
</style>
</head>
<body>
  <div class="banner">
    <svg class="headline" viewBox="0 0 1190 280" xmlns="http://www.w3.org/2000/svg">
      <text class="get" x="38" y="175" font-size="190" textLength="282" lengthAdjust="spacingAndGlyphs">Get</text>
      <text class="claim" x="343" y="115" font-size="122" textLength="780" lengthAdjust="spacingAndGlyphs">THE BEST PRICE</text>
      <text class="claim" x="343" y="187" font-size="92" textLength="415" lengthAdjust="spacingAndGlyphs">FOR YOUR</text>
      <text class="claim" x="768" y="187" font-size="72" textLength="355" lengthAdjust="spacingAndGlyphs">PROPERTY</text>
    </svg>
    <ul class="benefits">
      <li class="benefit">Feature Rich Marketing Solutions</li>
      <li class="benefit">Professional Tips, Tools and Strategies</li>
      <li class="benefit">0% Commission</li>
      <li class="benefit">No Hidden Charges</li>
    </ul>
  </div>
</body>
</html>
```